Therapy Dog Business need a brochure

I need a brochure designed for my Canine Assisted Therapy business in Victoria Australia. I have a logo already and info and photos to upload.
Best as white background and using the colours from the logo please
Updates

Hi Everyone,
I am sorry to have to revise the brief. I have added three new photos I was unable to add due to the size. I have had to wait for my photographer to change the size to add them today. I have been really inspired by all the work you have done so far. Thank you.
Could you please add the following on the brochure. (Under the individual dogs photo)
1. Pebble is the white dog. Please add the following under her picture. Pebble is one of the first Court Dogs in Australia. Working in Victoria, she has worked in the following Courts. The Inquest Tribunal of Norvale, The Petty Sessions Bench in Collingwood, and the Shire Tribunal in Melbourne CBD. Her ability to use her intuition for clients is inspiring. Please contact us for potential use in Courts. Pebble has worked at the Halden Constabulary College, and at KESTREL at Hal Con. She is a stunning dog!
2. Tobias is the golden dog. Tobias is Pebbles son, and had her instinct of intuition of who needs his help. Tobias has an incredible soft approach as does his mother Pebble. He is incredibly safe with young children, and yet has a playful nature for adolescents and adults alike. He is soft and caring, and like his mother will go to those who need him most. Tobias like his mother has worked at Halden Constabulary, his time at HC included the Halden Constabulary Command (HCC) Both he and his mother have very impressive CV'S!
3. Clover the black dog. Clover is my Therapy and Assistance dog "trainer" she is safe and stable with all the dogs and people I train for Therapy Dog Training and Assistance Dog Training. She has also been with me on my journey as a Counsellor and I have been able to work alongside her and Pebble for Counselling sessions.
She is soft, caring, and also intuitive. I am incredibly grateful for her help, as well as Pebble and Tobias.
ALSO I am so sorry to add this but could you also add the following: Maybe in dot point?
Court Dog Availability
Therapy Dog Visits - Lawyers - Courts - Child Protection
Police Station / Ambulance Station / Fire Station - Visits
Private Therapy Dog Sessions
website and email confirmation coming soon. Thank you

Target Market(s)

First Responders

Requirements
Must have
• All the photos provided.
Should not have
• Generic photos

```html
<!DOCTYPE html>
<html lang="en">
<head>
<meta charset="utf-8">
<title>Gentle Tails – Canine-Assisted Therapy Brochure</title>
<link href="https://fonts.googleapis.com/css2?family=Quicksand:wght@400;500;600;700&family=Oswald:wght@600&family=Great+Vibes&family=Poppins:ital,wght@1,700;1,800&display=swap" rel="stylesheet">
<style>
  :root{
    --backdrop:#2b2b2b;
    --paper:#ffffff;
    --maroon:#6a1831;
    --brick:#b2553a;
    --red:#d43d2d;
    --coral:#e07a78;
    --pink:#e98a8a;
    --orange:#f29a55;
    --heading:#454545;
    --body:#6d6d6d;
    --rule:#8a8a8a;
  }
  *{box-sizing:border-box;margin:0;padding:0}
  html,body{width:1200px;height:834px;overflow:hidden;background:var(--backdrop)}
  body{position:relative;font-family:"Quicksand",sans-serif}
  .page{position:absolute;top:64px;width:499px;height:706px;background:var(--paper);overflow:hidden}
  .page--front{left:94px}
  .page--back{left:607px}
  .abs{position:absolute}
  .shapes{position:absolute;left:0;top:0;width:499px;height:706px}

  /* front */
  .hero-kicker{left:27px;top:20px;color:#fff;font-family:"Quicksand",sans-serif;font-style:italic;font-weight:700;font-size:16px}
  .hero-title{left:26px;top:36px;color:#fff;font-family:"Oswald",sans-serif;font-weight:600;font-size:49px;line-height:1;letter-spacing:-.5px}
  .hero-script{left:30px;top:78px;color:#f7d9d9;font-family:"Great Vibes",cursive;font-size:70px;line-height:1}
  .brand-badge{left:336px;top:22px;width:156px;height:156px;border-radius:50%;background:#fff;display:flex;align-items:center;justify-content:center}
  .brand-badge .ring{width:138px;height:138px;border-radius:50%;border:3px solid var(--maroon);display:flex;align-items:center;justify-content:center}
  .brand-name{font-family:"Quicksand",sans-serif;font-weight:700;font-size:19px;color:var(--maroon);text-align:center;line-height:1.1}
  .cat-circle{left:277px;top:166px;width:226px;height:226px;border-radius:50%;background:linear-gradient(120deg,var(--red) 0%,#e0553a 50%,#f0a266 100%)}
  .cat-text{left:303px;top:178px;width:146px;text-align:center;color:#fff}
  .cat-text h2{font-weight:700;font-size:14px;line-height:14px;margin-bottom:4px}
  .cat-text p{font-weight:700;font-size:8.6px;line-height:10.1px}
  .dot{border-radius:50%}
  .benefits-title{left:28px;top:336px;color:var(--orange);font-weight:700;font-size:21px;line-height:21px;background:linear-gradient(90deg,var(--orange),#ec7d62);-webkit-background-clip:text;background-clip:text;-webkit-text-fill-color:transparent}
  .benefits-rule{left:0;top:382px;width:223px;height:1px;background:var(--rule)}
  .benefit{left:28px;width:462px}
  .benefit-head{display:flex;align-items:center;gap:7px;margin-left:0}
  .icon-dot{width:23px;height:23px;border-radius:50%;background:var(--coral);display:flex;align-items:center;justify-content:center;flex:none}
  .benefit h3{font-weight:700;font-size:12.4px;color:var(--heading)}
  .benefit p{font-weight:500;font-size:9.1px;line-height:11.8px;color:var(--body);margin-top:3px}
  .contact-phone{font-family:"Poppins",sans-serif;font-style:italic;font-weight:800;color:#fff;display:flex;align-items:center;gap:6px}
  .front-phone{left:28px;top:655px;font-size:26px}
  .front-web{left:259px;top:654px;color:#fff;font-family:"Poppins",sans-serif;font-style:italic;font-weight:700;font-size:15px;line-height:20px}

  /* back */
  .dog{left:19px;width:318px}
  .dog-head{display:flex;align-items:center;gap:7px;margin-left:0}
  .dog h3{font-weight:700;font-size:14.5px;color:var(--heading)}
  .dog p{font-weight:500;font-size:8.6px;line-height:10.9px;color:var(--body);margin-top:4px}
  .photo{border-radius:50%;border:4px solid #fff}
  .availability-pill{left:19px;top:312px;width:129px;height:16px;border-radius:8px;background:linear-gradient(90deg,var(--brick),var(--orange));color:#fff;font-weight:700;font-size:9.6px;line-height:16px;padding-left:7px}
  .avail-row{left:18px;font-size:10px;color:var(--heading);font-weight:500}
  .avail-row b{font-weight:700}
  .avail-row .bullet{color:var(--orange);margin:0 2px}
  .avail-rule{left:0;width:302px;height:1px;background:var(--rule)}
  .why-title{left:20px;top:406px;font-weight:700;font-size:20.5px;background:linear-gradient(90deg,var(--orange),var(--coral));-webkit-background-clip:text;background-clip:text;-webkit-text-fill-color:transparent}
  .reason{width:150px;text-align:center;color:#fff}
  .reason .badge{width:36px;height:36px;border-radius:50%;background:var(--orange);margin:0 auto 8px;display:flex;align-items:center;justify-content:center}
  .reason h4{font-weight:700;font-size:11.4px;line-height:12px}
  .reason p{font-weight:500;font-size:8.8px;line-height:11px;margin-top:5px}
  .journey{left:253px;top:577px;width:246px;height:97px;border-radius:48px 0 0 48px;background:var(--orange);color:#fff;text-align:center;padding:7px 10px 0 30px}
  .journey h4{font-family:"Poppins",sans-serif;font-style:italic;font-weight:800;font-size:11px}
  .journey p{font-weight:700;font-size:8.2px;line-height:10.2px;margin-top:2px}
  .back-phone{left:27px;top:645px;font-size:26px;color:var(--maroon)}
  .back-web{left:27px;top:675px;font-family:"Poppins",sans-serif;font-style:italic;font-weight:800;font-size:15.4px;color:var(--maroon)}
</style>
</head>
<body>

<section class="page page--front">
  <svg class="shapes" viewBox="0 0 499 706" aria-hidden="true">
    <defs>
      <linearGradient id="heroTone" x1="0" y1="0" x2="0" y2="1">
        <stop offset="0" stop-color="#a5452f"/>
        <stop offset=".45" stop-color="#8c4232"/>
        <stop offset=".6" stop-color="#6d86c9"/>
        <stop offset="1" stop-color="#7c95d6"/>
      </linearGradient>
      <linearGradient id="frontBand" x1="0" y1="0" x2="1" y2="0">
        <stop offset="0" stop-color="var(--brick)"/>
        <stop offset="1" stop-color="var(--pink)"/>
      </linearGradient>
    </defs>
    <path d="M0,0 H388 C405,45 440,85 499,110 V300 C380,345 200,350 0,282 Z" fill="url(#heroTone)"/>
    <path d="M0,640 C150,600 320,640 499,560 V706 H0 Z" fill="#e9918b"/>
    <path d="M0,652 C170,630 330,660 499,612 V706 H0 Z" fill="url(#frontBand)"/>
  </svg>
  <div class="abs" style="left:0;top:0;width:390px;height:300px" role="img" aria-label="Photo of three therapy dogs, two pale Labradors and a black Labrador, resting on a blue couch against a brick wall"></div>

  <p class="abs hero-kicker">Discover the Healing Power of</p>
  <h1 class="abs hero-title">Canine-Assisted</h1>
  <p class="abs hero-script">Therapy</p>

  <div class="abs brand-badge"><div class="ring"><span class="brand-name">Gentle<br>Tails</span></div></div>

  <div class="abs cat-circle" role="img" aria-label="Warm red-orange panel with a photo of a golden Labrador resting on a cushion"></div>
  <div class="abs cat-text">
    <h2>What is<br>Canine Assisted<br>Therapy?</h2>
    <p>Canine Assisted Therapy (CAT) is a unique form of therapy that integrates trained therapy dogs into the healing process. By working alongside licensed therapists, these compassionate and well-trained dogs help support individuals in overcoming emotional, physical, and psychological challenges. This innovative approach promotes healing, reduces stress, and enhances overall well-being.</p>
  </div>

  <span class="abs dot" style="left:262px;top:321px;width:17px;height:17px;background:var(--orange)"></span>

  <h2 class="abs benefits-title">Benefits of Canine<br>Assisted Therapy.</h2>
  <div class="abs benefits-rule"></div>

  <article class="abs benefit" style="top:393px">
    <div class="benefit-head"><span class="icon-dot"><svg width="11" height="11" viewBox="0 0 10 10"><circle cx="5" cy="5" r="4" fill="#fff"/></svg></span><h3>Emotional Support and Comfort</h3></div>
    <p>Therapy dogs provide immediate emotional support, offering comfort and companionship during therapy sessions. Their calming presence helps reduce feelings of anxiety, stress, depression, and grief, creating a safe and nurturing environment for healing.</p>
  </article>
  <article class="abs benefit" style="top:466px">
    <div class="benefit-head"><span class="icon-dot"><svg width="11" height="11" viewBox="0 0 10 10"><circle cx="5" cy="5" r="4" fill="#fff"/></svg></span><h3>Stress Relief and Relaxation</h3></div>
    <p>Interacting with dogs has been proven to reduce cortisol (stress hormone) levels and increase serotonin and oxytocin, the “feel-good” hormones. This natural relief from stress makes Canine Assisted Therapy an ideal option for individuals dealing with anxiety, trauma, PTSD, and grief.</p>
  </article>
  <article class="abs benefit" style="top:538px">
    <div class="benefit-head"><span class="icon-dot"><svg width="11" height="11" viewBox="0 0 10 10"><circle cx="5" cy="5" r="4" fill="#fff"/></svg></span><h3>Improved Mental Health</h3></div>
    <p>Therapy dogs encourage social interaction, communication, and emotional expression, helping individuals address mental health challenges such as depression, anxiety, PTSD, and grief. The unconditional love and companionship of a dog can foster trust and openness during therapy sessions.</p>
  </article>

  <p class="abs contact-phone front-phone">
    <svg width="22" height="22" viewBox="0 0 24 24"><circle cx="12" cy="12" r="10.5" fill="none" stroke="#fff" stroke-width="2"/><path d="M8.5 6.5l2 2.6-1.2 1.4c.8 1.7 2.1 3 3.8 3.8l1.4-1.2 2.6 2-1.2 2.2c-4.4-.3-8.7-4.6-9-9z" fill="#fff"/></svg>
    0400 000 123
  </p>
  <p class="abs front-web">www.gentletails.example<br>hello@gentletails.example</p>
</section>

<section class="page page--back">
  <svg class="shapes" viewBox="0 0 499 706" aria-hidden="true">
    <defs>
      <linearGradient id="whyTone" x1="0" y1="0" x2="0" y2="1">
        <stop offset="0" stop-color="var(--maroon)"/>
        <stop offset=".6" stop-color="#8a2c3a"/>
        <stop offset="1" stop-color="#c25a5c"/>
      </linearGradient>
    </defs>
    <path d="M0,404 q10,-9 21,0 t21,0 t21,0 t21,0 t21,0 t21,0 t21,0 t21,0 t21,0 t21,0 t21,0 t21,0 t21,0 t21,0 t21,0 t21,0 t21,0 t21,0 t21,0 t21,0 t21,0 t21,0 t21,0 t21,0 V600 H262 C200,705 80,660 0,585 Z" fill="url(#whyTone)"/>
    <path d="M0,585 C80,660 200,705 262,600" fill="none" stroke="var(--coral)" stroke-width="6"/>
  </svg>

  <div class="abs photo" style="left:337px;top:-25px;width:162px;height:162px;background:linear-gradient(160deg,#d96a48 0%,#e8dcc2 40%,#7d98d6 100%)" role="img" aria-label="Photo of Pebble, a pale Labrador, lying on a blue couch"></div>
  <div class="abs photo" style="left:310px;top:108px;width:136px;height:136px;background:linear-gradient(180deg,#b0563a 0%,#2a2a2e 55%,#7c95d6 100%)" role="img" aria-label="Photo of Clover, a black Labrador, lying on a blue couch"></div>
  <div class="abs photo" style="left:370px;top:220px;width:136px;height:136px;background:linear-gradient(160deg,#f1ede6 0%,#d98a5a 40%,#d8b071 60%,#7c95d6 100%)" role="img" aria-label="Photo of Tobias, a golden Labrador, resting on a blue couch"></div>

  <span class="abs dot" style="left:287px;top:113px;width:18px;height:18px;background:var(--coral)"></span>
  <span class="abs dot" style="left:463px;top:184px;width:16px;height:16px;background:var(--orange)"></span>

  <article class="abs dog" style="top:14px">
    <div class="dog-head"><span class="icon-dot"><svg width="11" height="11" viewBox="0 0 10 10"><circle cx="5" cy="5" r="4" fill="#fff"/></svg></span><h3>Pebble</h3></div>
    <p>Pebble is one of the first Court Dogs in Australia. Working in Victoria, she has worked in the following Courts. The Inquest Tribunal of Norvale, The Petty Sessions Bench in Collingwood, and the Shire Tribunal in Melbourne CBD. Her ability to use her intuition for clients is inspiring. Please contact us for potential use in Courts. Pebble has worked at the Halden Constabulary College, and at KESTREL at Hal Con. She is a stunning dog!</p>
  </article>
  <article class="abs dog" style="top:114px;width:290px">
    <div class="dog-head"><span class="icon-dot"><svg width="11" height="11" viewBox="0 0 10 10"><circle cx="5" cy="5" r="4" fill="#fff"/></svg></span><h3>Clover</h3></div>
    <p>Clover is my Therapy and Assistance dog "trainer" she is safe and stable with all the dogs and people I train for Therapy Dog Training and Assistance Dog Training. She has also been with me on my journey as a Counsellor and I have been able to work alongside her and Pebble for Counselling sessions. She is soft, caring, and also intuitive. I am incredibly grateful for her help, as well as Pebble and Tobias.</p>
  </article>
  <article class="abs dog" style="top:213px;width:340px">
    <div class="dog-head"><span class="icon-dot"><svg width="11" height="11" viewBox="0 0 10 10"><circle cx="5" cy="5" r="4" fill="#fff"/></svg></span><h3>Tobias</h3></div>
    <p>Tobias has his mothers instinct and intuition. Tobias has an incredible soft approach as does his mother Pebble. He is incredibly safe with young children, and yet has a playful nature for adolescents and adults alike. He is soft and caring, and like his mother will go to those who need him most. Tobias like his mother has worked at Halden Constabulary, his time at HC included the Halden Constabulary Command (HCC) Both he and his mother have very impressive CV'S!</p>
  </article>

  <div class="abs availability-pill">Court Dog Availability</div>
  <p class="abs avail-row" style="top:331px"><b>Therapy Dog Visits -</b> Lawyers - Courts - Child Protection</p>
  <div class="abs avail-rule" style="top:347px"></div>
  <p class="abs avail-row" style="top:351px;font-weight:600"><span class="bullet">•</span> Police Station <span class="bullet">•</span> Ambulance Station <span class="bullet">•</span> Fire Station</p>
  <div class="abs avail-rule" style="top:366px"></div>
  <p class="abs avail-row" style="top:370px"><b>Visits -</b> Private Therapy Dog Sessions</p>
  <div class="abs avail-rule" style="top:386px"></div>

  <h2 class="abs why-title">Why Choose Canine Assisted Therapy?</h2>

  <div class="abs reason" style="left:5px;top:439px">
    <div class="badge"><svg width="18" height="18" viewBox="0 0 24 24"><path d="M12 20s-7-4.4-7-9.5A3.8 3.8 0 0 1 12 8a3.8 3.8 0 0 1 7 2.5C19 15.6 12 20 12 20z" fill="#fff"/></svg></div>
    <h4>Proven<br>Effectiveness</h4>
    <p>Studies and testimonials highlight the positive effects therapy dogs have on emotional, psychological and physical health.</p>
  </div>
  <div class="abs reason" style="left:170px;top:439px;width:160px">
    <div class="badge"><svg width="16" height="16" viewBox="0 0 10 10"><circle cx="5" cy="5" r="3.5" fill="#fff"/></svg></div>
    <h4>Non-Invasive<br>and Gentle</h4>
    <p>Therapy dogs provide a natural and non-threatening way to engage with patients, making it accessible for individuals who may feel apprehensive about traditional therapy methods.</p>
  </div>
  <div class="abs reason" style="left:345px;top:439px">
    <div class="badge"><svg width="18" height="18" viewBox="0 0 24 24"><path d="M12 3l7 3v5c0 4.5-3 8-7 10-4-2-7-5.5-7-10V6z" fill="#fff"/><path d="M8.5 12l2.5 2.5 4.5-5" fill="none" stroke="var(--orange)" stroke-width="2.2" stroke-linecap="round" stroke-linejoin="round"/></svg></div>
    <h4>Safe and<br>Trustworthy</h4>
    <p>All therapy dogs are carefully trained to work with professionals, ensuring that interactions are safe, beneficial, and appropriate for all individuals.</p>
  </div>

  <div class="abs journey">
    <h4>Join the Healing Journey Today!</h4>
    <p>Whether you are seeking emotional support or mental health improvement, Canine Assisted Therapy offers a unique and compassionate approach to healing. Connect with us today to learn more about how a therapy dog can help enhance your life and well-being.</p>
  </div>

  <p class="abs contact-phone back-phone">
    <svg width="22" height="22" viewBox="0 0 24 24"><circle cx="12" cy="12" r="10.5" fill="none" stroke="var(--maroon)" stroke-width="2"/><path d="M8.5 6.5l2 2.6-1.2 1.4c.8 1.7 2.1 3 3.8 3.8l1.4-1.2 2.6 2-1.2 2.2c-4.4-.3-8.7-4.6-9-9z" fill="var(--maroon)"/></svg>
    0400 000 123
  </p>
  <p class="abs back-web">www.gentletails.example | hello@gentletails.example</p>
</section>

</body>
</html>
```